Thank you for exploring whether you are interested in creating a book cover for the Insight Lantern!

The cover should look professional yet appeal to a person who is open to approaching life more deeply.

The logo that I've uploaded is something that you are welcome to use in your book cover design but is not required to be the primary graphic.

The following is a description of the Insight Lantern and its purpose.
RADICAL CLARITY IS POSSIBLE

Are you tired of hitting up against your limitations? Do you wish you could be more effective in everything you do? What would it be like if you could walk confidently into any situation and automatically comprehend it, organize your thoughts, and respond creatively? This kind of radical clarity is not only possible, it’s right in front of you—and The Insight Lantern: Notice What Matters. Hold Bold Dialogues. Build the Days You Crave. shows you the pathway to get there!

In the book, Dr. Lorne Haskett draws on over 30 years of experience with executive coaching and leadership development to deliver priceless wisdom about how to see clearly in today’s complex and uncertain world. Using his Insight Lantern, you’ll discover where you’re stuck and why, find your authentic direction, and learn to engage creatively with life so you can start getting what you really want.

A TRANSFORMATIONAL TOOL

The Insight Lantern is a cutting-edge leadership development tool that supports you to activate your maximum potential, both personally and professionally. It’s based on the idea that there are four fundamental building blocks to reality: Intentions, Actions, Facts, and Stories. Understanding the differences between these dimensions of your experience and learning how they work together is the key to forging a clear path toward your destination in life. The Insight Lantern organizes these four main building blocks around the two polarities of a compass:

1. North to South – Intentions to Actions
We all have billions of intentions, but how many do we actually put into action? In this polarity you learn to notice and implement your intentions in order to generate more effective actions and create meaningful outcomes in your life.

2. East vs. West – Facts vs. Stories
We all create stories to make sense of life, but how many of us actually get clear on the facts to see where our stories might be off? In this polarity you learn to discern the objective facts from your subjective interpretations and stories, illuminating a clearer perspective to uncover what’s been blocking you on the path to success.

Using the Insight Lantern you’ll discover how naming and implementing your intentions in life naturally results in more effective behavior and actions, and how distinguishing the real facts from your interpretations of any situation can propel you toward radical clarity and true fulfillment.

BOLD DIALOGUES

The key benefit of using the Insight Lantern is that you’ll have more of what Lorne calls “Bold Dialogues.” Bold dialogues are those that move you closer to what you’re wanting in life—the kind of human-to-human interactions that actually make a difference. By applying the Insight Lantern, you gain critical insight that opens your eyes to new opportunities for Bold Dialogues, helping you draw on your imagination and move beyond your current stance toward a positive outcome. Every conversation is a possibility waiting to be discovered. The more Bold Dialogues you have, the more profound and meaningful shifts you activate in your life.

PRACTICAL GUIDANCE

The book doesn’t just give you a theoretical understanding of how to gain more clarity in your life. Dr. Haskett provides you with clear, practical steps to develop the core competencies you need to start getting the results you want. As you explore the book, you’ll find:

• A thorough description of all the directions of the Insight Lantern, each with three main points to focus your energy on.
• Case studies from Lorne’s many clients who have successfully used the Insight Lantern to transform their own lives.
• Hands-on practices Lorne has developed to help you put your new skills to use immediately.
• Step-by-step guidance to apply the Insight Lantern in any situation, including real-life stories from people who have experienced genuine transformation using this tool.

The Insight Lantern will help you to deepen your understanding of the challenges in your life, integrate new competencies to boost your effectiveness, and awaken to exciting opportunities for your own growth, leadership, and success!

ABOUT THE AUTHOR

Dr. Lorne Haskett has over 30 years of experience with leadership development and executive coaching work. As owner and principal coach of Haskett Leadership Consultants, he has been integrating the fields of management consulting, business psychology, and leadership coaching since 1983. Lorne holds a Ph.D. in psychodynamic and group psychology from the Merrowind Graduate Institute, an M.A. in human growth and potential from the University of Fallbrook Ridge, and a B.A. in accounting and Business Administration from Kestrel Vale University. He is the creator of the Insight Lantern™, a leadership development tool that supports people to see life clearly, wake up to exciting opportunities for their own growth and leadership, and take empowered action toward true success. Lorne’s combination of business expertise, human compassion, and incisive questions help his clients achieve unprecedented results.

Target Market(s)

Out intended audience is folks who would like to be more effective and to grow and transform. This being more productive and developing could be in their careers or their personal lives.

Industry/Entity Type

It Professional

Requirements
Must have
• Stock images, if used, that I can purchase exclusively or that you can easily create specifically for the book once you are the chosen designer. I completely understand using stock imaging in your submissions pre-selection.
Nice to have
• Ideally the cover will include both the title and subtitle.

```html
<!DOCTYPE html>
<html lang="en">
<head>
<meta charset="utf-8">
<title>The Insight Lantern – Book Cover</title>
<link href="https://fonts.googleapis.com/css2?family=Montserrat:wght@400;500;600&family=Nunito+Sans:ital,wght@0,400;0,700;1,400&display=swap" rel="stylesheet">
<style>
  :root {
    --page-bg: #e9e8e5;
    --cover-black: #050506;
    --brand-blue: #29a9e1;
    --rule-blue: #2a7fc0;
    --text-light: #e6e6e6;
    --text-muted: #c9c9c9;
    --box-line: #3d4a7a;
  }
  * { box-sizing: border-box; margin: 0; padding: 0; }
  html, body {
    width: 1200px; height: 800px; overflow: hidden;
    background: var(--page-bg);
  }
  .cover-set {
    position: relative; width: 1200px; height: 800px;
    display: flex; justify-content: center; align-items: center; gap: 30px;
  }
  .back-cover, .spine, .front-cover {
    background: var(--cover-black); height: 660px; position: relative;
    color: var(--text-light);
  }

  /* Back cover */
  .back-cover { width: 440px; padding: 40px 28px 0 34px; font-family: "Nunito Sans", sans-serif; }
  .back-heading {
    font-family: "Montserrat", sans-serif; font-weight: 400; font-size: 17px;
    letter-spacing: 3.2px; text-align: center; color: #fff;
  }
  .back-rule { height: 1px; background: var(--rule-blue); margin: 14px 0 14px 0; }
  .back-blurb { font-size: 10.4px; line-height: 1.75; color: var(--text-muted); }
  .back-blurb strong { color: var(--brand-blue); font-weight: 700; }
  .praise { margin-top: 20px; }
  .praise-item { margin-bottom: 10px; }
  .praise-quote { font-size: 10.4px; line-height: 1.75; color: var(--text-muted); }
  .praise-by {
    text-align: center; font-style: italic; color: var(--brand-blue);
    font-size: 10.4px; line-height: 1.15;
  }
  .back-footer {
    position: absolute; left: 32px; right: 28px; bottom: 24px;
    display: flex; justify-content: space-between; align-items: flex-end;
  }
  .footer-box {
    width: 106px; height: 55px; border: 1.5px solid var(--box-line);
    display: flex; align-items: center; justify-content: center;
    font-family: "Montserrat", sans-serif; font-size: 10.5px; letter-spacing: 2px; color: #9a9a9a;
    margin-bottom: 16px;
  }
  .back-mark { text-align: center; display: flex; flex-direction: column; align-items: center; gap: 6px; }
  .back-mark-circle { width: 40px; height: 40px; border-radius: 50%; border: 2px solid var(--brand-blue); }
  .back-mark-name {
    font-family: "Nunito Sans", sans-serif; color: var(--brand-blue);
    font-size: 10.5px; line-height: 1.1; text-transform: uppercase;
  }

  /* Spine */
  .spine { width: 38px; display: flex; flex-direction: column; align-items: center; padding-top: 34px; }
  .spine-circle { width: 24px; height: 24px; border-radius: 50%; border: 2px solid var(--brand-blue); flex: none; }
  .spine-title {
    writing-mode: vertical-rl; font-family: "Montserrat", sans-serif; font-weight: 600;
    font-size: 14px; letter-spacing: 1.4px; margin-top: 22px; white-space: nowrap;
  }
  .spine-title .spine-author { color: var(--brand-blue); margin-bottom: 18px; }
  .spine-title .spine-book { color: #fff; }
  .spine-publisher {
    position: absolute; bottom: 26px; left: 50%; transform: translateX(-50%);
    writing-mode: vertical-rl;
    font-family: "Montserrat", sans-serif; font-size: 8.5px; line-height: 1.05; color: var(--brand-blue);
    text-transform: uppercase; text-align: left; white-space: nowrap;
  }

  /* Front cover */
  .front-cover { width: 440px; padding: 34px 26px 0; font-family: "Montserrat", sans-serif; }
  .front-author { font-size: 22px; letter-spacing: 3px; color: #fff; text-align: right; font-weight: 400; }
  .front-coauthors { font-size: 11px; letter-spacing: 2.4px; color: var(--text-muted); text-align: right; margin-top: 2px; text-transform: uppercase; }
  .front-rule { height: 1.5px; background: var(--rule-blue); margin: 8px 0 4px; }
  .front-title {
    color: var(--brand-blue); font-weight: 400; font-size: 60px; line-height: 1.0;
    letter-spacing: -1px; text-transform: uppercase;
  }
  .front-title span { display: block; }
  .front-title .line-two { font-size: 64px; padding-left: 20px; }
  .front-emblem {
    margin: 26px auto 0; width: 250px; height: 250px; border-radius: 50%;
    border: 26px solid var(--brand-blue); display: flex; align-items: center; justify-content: center;
  }
  .front-emblem-name {
    font-size: 20px; color: var(--brand-blue); text-transform: uppercase; letter-spacing: 2px;
    text-align: center; line-height: 1.3;
  }
  .front-tagline {
    position: absolute; left: 0; right: 0; bottom: 40px; text-align: center;
    font-size: 16px; letter-spacing: 2.6px; line-height: 1.9; color: #fff; text-transform: uppercase;
  }
</style>
</head>
<body>
<main class="cover-set">

  <section class="back-cover" aria-label="Back cover">
    <h2 class="back-heading">RADICAL CLARITY IS POSSIBLE</h2>
    <div class="back-rule"></div>
    <p class="back-blurb"><strong>Dr. Lorne Haskett</strong> and more of the same this is praise for Dr. Haskett's new book lorem ipsum greeeking and you will see more clearly loremipsum . Lorem ipsum greeking and more of the same this is praise for Dr. Haskett's new book lorem ipsum greeeking and you will see more clearly lorem ipsum and more to see. Lorem ipsum greeking and more of the same this is praise for Dr. Haskett's new book lorem ipsum greeeking.</p>

    <div class="praise">
      <div class="praise-item">
        <p class="praise-quote">“Lorem ipsum greeking and more of the same this is praise for Dr. Haskett's new book lorem ipsum greeeking and you will see more clearly lorem ipsum.”</p>
        <p class="praise-by">- Calvin Ostrander<br>Director of Lorem Isum Center</p>
      </div>
      <div class="praise-item">
        <p class="praise-quote">“Lorem ipsum greeking and more of the same this is praise for Dr. Haskett's new book lorem ipsum greeeking and you will see more clearly lorem ipsum.”</p>
        <p class="praise-by">- Marisol Featherly<br>Director of Lorem Isum Center</p>
      </div>
      <div class="praise-item">
        <p class="praise-quote">“Lorem ipsum greeking and more of the same this is praise for Dr. Haskett's new book lorem ipsum greeeking and you will see more clearly lorem ipsum.”</p>
        <p class="praise-by">- Calvin Ostrander<br>Director of Lorem Isum Center</p>
      </div>
      <div class="praise-item">
        <p class="praise-quote">“Lorem ipsum greeking and more of the same this is praise for Dr. Haskett's new book lorem ipsum greeeking and you will see more clearly lorem ipsum.”</p>
        <p class="praise-by">- Marisol Featherly<br>Director of Lorem Isum Center</p>
      </div>
    </div>

    <div class="back-footer">
      <div class="footer-box">PUBLISHER</div>
      <div class="back-mark">
        <div class="back-mark-circle"></div>
        <p class="back-mark-name">The Insight<br>Lantern</p>
      </div>
      <div class="footer-box">UPC CODE</div>
    </div>
  </section>

  <section class="spine" aria-label="Spine">
    <div class="spine-circle"></div>
    <p class="spine-title"><span class="spine-author">DR. LORNE HASKETT</span><span class="spine-book">THE INSIGHT LANTERN</span></p>
    <p class="spine-publisher">Quillbrook<br>Publishing</p>
  </section>

  <section class="front-cover" aria-label="Front cover">
    <p class="front-author">DR. LORNE HASKETT</p>
    <p class="front-coauthors">Wren Halloway and Tobin Marsh</p>
    <div class="front-rule"></div>
    <h1 class="front-title"><span>The Insight</span><span class="line-two">Lantern</span></h1>
    <div class="front-emblem">
      <p class="front-emblem-name">Insight<br>Lantern</p>
    </div>
    <p class="front-tagline">Notice what matters.<br>Hold bold dialogues.<br>Build the days you crave.</p>
  </section>

</main>
</body>
</html>
```